I need a design to display a result on a range line

For example - If I have a blood sugar result and I want to display it on a line so that I can display it in picture terms so that it can be understood more.
I want to input the result in a calculator so it can be displayed on the range line.

I want it so I can customise it and apply it to other results my self too.

```html
<!DOCTYPE html>
<html lang="en">
<head>
<meta charset="utf-8">
<title>Blood Sugar Range Line</title>
<link rel="stylesheet" href="https://fonts.googleapis.com/css2?family=Hind:wght@400;600;700&display=swap">
<style>
  :root {
    --bg: #ffffff;
    --ink: #000000;
    --unit: #a6a6a6;
    --tick: #7a7a7a;
    --red: #ff0000;
    --orange: #ff9900;
    --yellow: #ffff00;
    --green: #1aff50;
    --lime: #7fff2a;
    --marker: #000000;
  }
  * { margin: 0; padding: 0; box-sizing: border-box; }
  html, body { width: 1200px; height: 900px; overflow: hidden; background: var(--bg); }
  body { font-family: "Hind", sans-serif; color: var(--ink); }
  .canvas { position: relative; width: 1200px; height: 900px; }

  .range-bar {
    position: absolute; left: 135px; width: 916px; height: 54px; border-radius: 27px;
    background: linear-gradient(90deg,
      var(--red) 0%, var(--red) 5%, var(--orange) 17%, var(--yellow) 26%,
      var(--green) 30%, var(--green) 44%, var(--lime) 48%, var(--yellow) 54%,
      var(--orange) 67%, #ff4a00 77%, var(--red) 84%, var(--red) 100%);
  }
  .range-bar--labelled { top: 240px; }
  .range-bar--dot { top: 548px; }

  .tick { position: absolute; width: 1px; background: var(--tick); }
  .tick--top { top: 191px; height: 49px; }
  .tick--bottom { top: 512px; height: 36px; }

  .limit { position: absolute; font-size: 20px; line-height: 1; white-space: nowrap; }
  .limit--top { top: 188px; font-weight: 400; }
  .limit--bottom { top: 509px; font-weight: 700; }
  .unit { font-size: 14px; font-weight: 700; color: var(--unit); margin-left: 3px; }

  .zone-in { position: absolute; top: 257px; font-size: 20px; font-weight: 700; line-height: 1; transform: translateX(-50%); white-space: nowrap; }
  .zone-under { position: absolute; top: 616px; font-size: 20px; font-weight: 400; line-height: 1; transform: translateX(-50%); white-space: nowrap; }

  .pointer { position: absolute; left: 491px; top: 298px; width: 32px; height: 34px; }
  .result-value { position: absolute; top: 343px; left: 512px; transform: translateX(-50%); font-size: 20px; font-weight: 700; line-height: 1; white-space: nowrap; }

  .result-dot { position: absolute; left: 517px; top: 562px; width: 32px; height: 32px; border-radius: 50%; background: var(--marker); }
  .result-inline { position: absolute; left: 559px; top: 568px; font-size: 20px; font-weight: 700; line-height: 1; white-space: nowrap; }
</style>
</head>
<body>
<div class="canvas">

  <section class="range-line range-line--labelled">
    <span class="limit limit--top" style="right:827px">3.99<span class="unit">mmol/L</span></span>
    <span class="tick tick--top" style="left:383px"></span>
    <span class="limit limit--top" style="left:390px">4.0</span>

    <span class="limit limit--top" style="right:618px">5.59<span class="unit">mmol/L</span></span>
    <span class="tick tick--top" style="left:594px"></span>
    <span class="limit limit--top" style="left:601px">5.6</span>

    <span class="limit limit--top" style="right:408px">6.99<span class="unit">mmol/L</span></span>
    <span class="tick tick--top" style="left:804px"></span>
    <span class="limit limit--top" style="left:811px">7</span>

    <div class="range-bar range-bar--labelled"></div>
    <span class="zone-in" style="left:277px">Low</span>
    <span class="zone-in" style="left:491px">Optimal</span>
    <span class="zone-in" style="left:709px">Pre-Diabetic</span>
    <span class="zone-in" style="left:929px">High</span>

    <svg class="pointer" viewBox="0 0 32 34" aria-hidden="true"><polygon points="16,0 32,34 0,34" fill="var(--lime)"/></svg>
    <span class="result-value">5.19<span class="unit">mmol/L</span></span>
  </section>

  <section class="range-line range-line--dot">
    <span class="limit limit--bottom" style="right:827px">3.99<span class="unit">mmol/L</span></span>
    <span class="tick tick--bottom" style="left:383px"></span>
    <span class="limit limit--bottom" style="left:390px">4.0</span>

    <span class="limit limit--bottom" style="right:613px">5.59<span class="unit">mmol/L</span></span>
    <span class="tick tick--bottom" style="left:594px"></span>
    <span class="limit limit--bottom" style="left:601px">5.6</span>

    <span class="limit limit--bottom" style="right:403px">6.99<span class="unit">mmol/L</span></span>
    <span class="tick tick--bottom" style="left:804px"></span>
    <span class="limit limit--bottom" style="left:811px">7</span>

    <div class="range-bar range-bar--dot"></div>
    <span class="result-dot"></span>
    <span class="result-inline">5.19<span class="unit">mmol/L</span></span>

    <span class="zone-under" style="left:252px">Low</span>
    <span class="zone-under" style="left:496px">Optimal</span>
    <span class="zone-under" style="left:716px">Pre-Diabetic</span>
    <span class="zone-under" style="left:938px">High</span>
  </section>

</div>
</body>
</html>
```